Business card for law firm

Need business card for new law firm. Think confident, authoritative, conservative, but not stuffy or old-fashioned.

Contact Information for Business Card

Content for card - logo (uploaded), plus the following:

Paul Wexbury (larger font)
Managing Partner (larger font, but not as large as name)
Level 9, 41 Tansy Lane
Sydney NSW 2000
Main Tel 02 7346 2190
Direct Tel 02 6273 4415
Email paul@qvlegal.com.au
www.qvlegal.com.au

Letterhead design should include logo plus:
Level 9, 41 Tansy Lane
Sydney NSW 2000
Tel 02 6273 4415
www.qvlegal.com.au

```html
<!DOCTYPE html>
<html lang="en">
<head>
<meta charset="utf-8">
<title>Quayvale Legal — Letterhead</title>
<link rel="stylesheet" href="https://fonts.googleapis.com/css2?family=Cormorant+Garamond:wght@500&family=Didact+Gothic&family=Roboto:wght@300;400&display=swap">
<style>
  :root {
    --backdrop: #e4e5e7;
    --paper-top: #f7f7f8;
    --paper-bottom: #ebecee;
    --navy: #0f1f4f;
    --black: #050505;
    --ink: #1b1b1b;
    --body-ink: #5a5a5a;
    --salutation-ink: #555555;
    --signature-blue: #c9d7ee;
    --white: #ffffff;
  }
  * { box-sizing: border-box; margin: 0; padding: 0; }
  html, body {
    width: 1024px;
    height: 1200px;
    overflow: hidden;
    background: var(--backdrop);
  }
  .letterhead {
    position: absolute;
    left: 88px;
    top: 0;
    width: 848px;
    height: 1200px;
    background: linear-gradient(180deg, var(--paper-top), var(--paper-bottom));
    box-shadow: 0 0 24px rgba(0, 0, 0, 0.12);
  }
  .header-block {
    position: absolute;
    left: 0;
    top: 74px;
    width: 139px;
    height: 44px;
    background: var(--black);
  }
  .contact-band {
    position: absolute;
    left: 182px;
    top: 74px;
    width: 666px;
    height: 48px;
    background: var(--navy);
    color: var(--white);
    font-family: "Roboto", Arial, sans-serif;
    font-weight: 400;
    font-size: 15px;
    line-height: 48px;
    text-align: right;
    padding-right: 72px;
    letter-spacing: 0.1px;
  }
  .firm-name {
    position: absolute;
    left: 76px;
    top: 132px;
    font-family: "Cormorant Garamond", Georgia, serif;
    font-weight: 500;
    font-size: 29px;
    letter-spacing: 1.5px;
    text-transform: uppercase;
    color: var(--ink);
  }
  .letter {
    position: absolute;
    left: 79px;
    top: 312px;
    width: 698px;
  }
  .salutation {
    font-family: "Roboto", Arial, sans-serif;
    font-weight: 300;
    font-size: 22px;
    color: var(--salutation-ink);
    margin-bottom: 34px;
  }
  .letter-body p {
    font-family: "Didact Gothic", "Century Gothic", sans-serif;
    font-size: 12px;
    line-height: 14.6px;
    color: var(--body-ink);
    text-align: justify;
    margin-bottom: 14.6px;
  }
  .closing {
    font-family: "Didact Gothic", "Century Gothic", sans-serif;
    font-size: 12px;
    color: var(--body-ink);
    margin-top: 30px;
  }
  .signature {
    display: block;
    margin-top: 44px;
    width: 146px;
    height: 66px;
    border-radius: 8px;
    background: linear-gradient(90deg, var(--signature-blue), rgba(201, 215, 238, 0.45));
  }
</style>
</head>
<body>
  <main class="letterhead">
    <div class="header-block"></div>
    <div class="contact-band">Level 9, 41 Tansy Lane, Sydney NSW 2000 | 02 6273 4415 | www.qvlegal.com.au</div>
    <div class="firm-name">Quayvale Legal</div>

    <section class="letter">
      <h1 class="salutation">Dear Mr. Harlow,</h1>
      <div class="letter-body">
        <p>Lorem ipsum dolor sit amet, consectetur adipiscing elit. Donec orci purus, luctus vitae dignissim eu, iaculis sed purus. Vivamus faucibus, ipsum nec aliquet viverra, leo mauris condimentum ligula, sit amet sagittis enim ligula quis arcu. Nam egestas tortor id nisi porttitor mattis. In tortor ante, ultricies in suscipit a, tempus non massa. Vivamus et auctor mi. Fusce vel massa nulla. Phasellus nec eros mauris, et scelerisque orci.</p>
        <p>Donec malesuada orci vitae nulla accumsan porta a id massa. Quisque accumsan iaculis magna sit amet fringilla. Maecenas consequat, magna eget tincidunt semper, odio nibh rutrum mi, id feugiat ante nisi eu risus. Vestibulum nunc orci, rhoncus a placerat in, ultricies in mi. Cras mattis varius eros, vel fringilla nisi suscipit eget. Quisque scelerisque sagittis nulla at porttitor.</p>
        <p>Sed id augue vitae urna euismod commodo aliquet a quam. Pellentesque arcu velit, cursus et malesuada ut, consequat et diam. Nullam erat sem, rhoncus id ullamcorper vitae, rhoncus et arcu. In ultricies ultricies nulla, ut rutrum nisi iaculis at. Donec eu magna a metus ornare faucibus. Fusce aliquet faucibus ultricies. Morbi semper, est id tincidunt gravida, sem arcu adipiscing lacus, ac bibendum nulla leo eu purus. Quisque nec diam sed risus consectetur accumsan quis quis nibh. Vestibulum id purus lorem.</p>
        <p>It is a long established fact that a reader will be distracted by the readable content of a page when looking at its layout. The point of using Lorem Ipsum is that it has a more-or-less normal distribution of letters, as opposed to using 'Content here, content here', making it look like readable English. Many desktop publishing packages</p>
      </div>
      <p class="closing">Sincerely,</p>
      <span class="signature" role="img" aria-label="Handwritten signature of the sender in blue ink"></span>
    </section>
  </main>
</body>
</html>
```